Halvorsen Winery Wine Label Re-design

Halvorsen Winery is located in the Finger Lakes region of New York. The Halvorsen Family planted the first vineyards in 1979 and opened in 1986. We produce award winning premium, hand crafted estate grown wines. We are in the process of a wine label re-design across our entire line. We would like to have the new label 'pop' but still convey elegance and ultra-premium quality. We are open to all color and styles or a minimalist design.
The attached files contain our new logo and samples of our current label (marked current) with dimensions. Our labeler is limited to label shapes but does not necessarily to have to be die-cut(the top arch) like our current label.

Target Market(s)

Upper income quality wine drinkers

Colors

Designer to choose colors to be used in the design.

Requirements
Should not have
• Should not be a tranparent label

```html
<!DOCTYPE html>
<html lang="en">
<head>
<meta charset="utf-8">
<title>Halvorsen Winery – Wine Labels</title>
<link rel="stylesheet" href="https://fonts.googleapis.com/css2?family=Cormorant+Garamond:wght@500&family=Pinyon+Script&family=Oswald:wght@400&family=Playfair+Display:wght@400&display=swap">
<style>
  :root {
    --backdrop: #b5bfbb;
    --label-black: #050304;
    --ink-white: #ffffff;
    --band-plum: #2d0e1f;
    --cabernet: #7b1e32;
    --chardonnay: #2f6b22;
  }
  html, body {
    margin: 0;
    padding: 0;
    overflow: hidden;
  }
  body {
    width: 1200px;
    height: 904px;
    background: var(--backdrop);
    position: relative;
  }
  .label {
    position: absolute;
    top: 124px;
    width: 445px;
    height: 659px;
    background: var(--label-black);
    color: var(--ink-white);
    overflow: hidden;
  }
  .label--cabernet { left: 122px; --accent: var(--cabernet); }
  .label--chardonnay { left: 634px; --accent: var(--chardonnay); }

  .label__emblem {
    position: absolute;
    top: 26px;
    left: 50%;
    width: 60px;
    height: 60px;
    margin-left: -32px;
    border: 2px solid var(--ink-white);
    border-radius: 50%;
  }
  .label__brand {
    position: absolute;
    top: 108px;
    left: 0;
    right: 0;
    text-align: center;
    font-family: "Cormorant Garamond", serif;
    font-weight: 500;
    color: var(--ink-white);
    line-height: 1;
  }
  .label__brand-name {
    display: block;
    font-size: 46px;
    letter-spacing: 7px;
    padding-left: 7px;
  }
  .label__brand-sub {
    display: block;
    margin-top: 4px;
    font-size: 21px;
    letter-spacing: 11px;
    padding-left: 11px;
  }
  .label__artwork {
    position: absolute;
    top: 190px;
    left: 0;
    right: 0;
    height: 410px;
    background:
      radial-gradient(ellipse at 30% 25%, var(--accent) 0%, transparent 45%),
      radial-gradient(ellipse at 80% 80%, var(--accent) 0%, transparent 55%),
      linear-gradient(180deg, rgba(0,0,0,0) 0%, var(--accent) 100%);
    opacity: 0.75;
  }
  .label__varietal {
    position: absolute;
    top: 292px;
    left: 0;
    right: 0;
    margin: 0;
    text-align: center;
    font-family: "Pinyon Script", cursive;
    font-weight: 400;
    font-size: 68px;
    line-height: 64px;
    color: var(--ink-white);
  }
  .label__vintage {
    position: absolute;
    top: 476px;
    left: 0;
    right: 0;
    text-align: center;
    font-family: "Playfair Display", serif;
    font-size: 42px;
    line-height: 1;
  }
  .label__band {
    position: absolute;
    left: 0;
    right: 0;
    bottom: 0;
    height: 59px;
    background: var(--band-plum);
    display: flex;
    align-items: center;
    justify-content: space-between;
    padding: 0 18px 0 14px;
    font-family: "Oswald", sans-serif;
    font-size: 17px;
    letter-spacing: 0.3px;
  }
</style>
</head>
<body>
  <article class="label label--cabernet">
    <div class="label__emblem"></div>
    <div class="label__brand">
      <span class="label__brand-name">HALVORSEN</span>
      <span class="label__brand-sub">WINERY</span>
    </div>
    <div class="label__artwork" role="img" aria-label="Engraved grape cluster with curling vine leaves in deep wine red"></div>
    <h2 class="label__varietal">Cabernet<br>Sauvignon</h2>
    <div class="label__vintage">2013</div>
    <footer class="label__band">
      <span class="label__abv">Alc. 15% BY VOL.</span>
      <span class="label__volume">750ML</span>
    </footer>
  </article>

  <article class="label label--chardonnay">
    <div class="label__emblem"></div>
    <div class="label__brand">
      <span class="label__brand-name">HALVORSEN</span>
      <span class="label__brand-sub">WINERY</span>
    </div>
    <div class="label__artwork" role="img" aria-label="Engraved grape cluster with curling vine leaves in vine green"></div>
    <h2 class="label__varietal">Reserve<br>Chardonnay</h2>
    <div class="label__vintage">2014</div>
    <footer class="label__band">
      <span class="label__abv">Alc. 15% BY VOL.</span>
      <span class="label__volume">750ML</span>
    </footer>
  </article>
</body>
</html>
```